Halvorine Ledgers & Advisory Tri-Fold Brochure (8.5"x11")

I need a professional looking brochure for my bookkeeping business. I am looking for something professional yet casual (not too corporate looking). I have attached a sample brochure that will outline the areas and a copy of our logo. I'd like to stick with shades of blue. The final product should communicate professional and personal.

Target Market(s)

Small service businesses.

Industry/Entity Type

Business

Font styles to use
Sans Serif

Requirements
Must have
• Professional looking photos of people in areas where it asks for a picture.

```html
<!DOCTYPE html>
<html lang="en">
<head>
<meta charset="utf-8">
<title>Halvorine Ledgers &amp; Advisory – Brochure Panel</title>
<link rel="stylesheet" href="https://fonts.googleapis.com/css2?family=Arimo:wght@400;700&family=Tinos:wght@700&display=swap">
<style>
  :root {
    --gold-top: #f7d437;
    --gold-mid: #f4c22a;
    --gold-deep: #f0a81c;
    --lime-tint: #e3e86a;
    --sky-light: #cfe9fb;
    --sky: #7cc4ef;
    --ocean: #1a8fd6;
    --navy: #173a86;
    --slate: #6d7780;
    --slate-dark: #55606a;
    --ink: #1f1f1f;
    --white: #ffffff;
    --service-head: #f6c56a;
  }
  * { margin: 0; padding: 0; box-sizing: border-box; }
  html, body { width: 809px; height: 1200px; overflow: hidden; background: var(--white); }
  h1, h2 { font-weight: 400; }
  .brochure {
    position: relative;
    width: 809px; height: 1200px;
    overflow: hidden;
    font-family: "Arimo", Arial, sans-serif;
    color: var(--ink);
    background: var(--white);
  }

  /* ---------- top band ---------- */
  .top-band {
    position: absolute; left: 0; top: 0; width: 809px; height: 494px;
    background: linear-gradient(90deg, var(--gold-top) 0%, var(--gold-mid) 55%, var(--lime-tint) 78%, var(--sky-light) 100%);
  }
  .side-stripes {
    position: absolute; top: 0; right: 0; width: 150px; height: 1200px;
    background: linear-gradient(90deg, var(--sky-light) 0 28%, var(--sky) 28% 48%, var(--ocean) 48% 62%, var(--slate) 62% 100%);
  }
  .intro-box {
    position: absolute; left: 0; top: 0; width: 437px; height: 459px;
    background: linear-gradient(180deg, var(--gold-top), var(--gold-deep));
    border-right: 2px solid rgba(255,255,255,0.7);
    border-bottom: 2px solid rgba(255,255,255,0.7);
    padding: 40px 22px 0 22px;
    text-align: center;
  }
  .intro-title {
    color: var(--white);
    font-size: 25px; line-height: 1.1;
    text-transform: uppercase;
  }
  .intro-sub {
    margin-top: 12px;
    color: var(--ink);
    font-size: 18px; font-weight: 700;
    text-transform: uppercase;
  }
  .intro-copy {
    margin-top: 8px;
    font-size: 17px; font-weight: 700; line-height: 29px;
    text-align: justify;
    color: var(--ink);
  }

  .why-title {
    position: absolute; left: 458px; top: 26px;
    font-size: 24px; color: var(--navy);
    white-space: nowrap;
  }
  .benefits {
    position: absolute; left: 478px; top: 150px;
    list-style: none;
  }
  .benefits li {
    font-size: 40px; line-height: 45px;
    color: var(--ink);
    display: flex; align-items: center;
    white-space: nowrap;
  }
  .benefits li::before {
    content: ""; width: 14px; height: 14px; border-radius: 50%;
    background: var(--ink); margin-right: 16px;
  }

  /* ---------- services band ---------- */
  .services-band {
    position: absolute; left: 0; top: 494px; width: 809px; height: 425px;
    background:
      radial-gradient(ellipse at 20% 30%, rgba(255,255,255,0.55), transparent 45%),
      radial-gradient(ellipse at 80% 70%, rgba(255,255,255,0.35), transparent 50%),
      linear-gradient(160deg, var(--ocean) 0%, var(--sky) 45%, var(--ocean) 100%);
  }
  .services {
    position: absolute; left: 297px; top: 504px;
  }
  .services-title {
    font-size: 32px; color: var(--service-head);
    line-height: 36px;
  }
  .services-list { list-style: none; }
  .services-list li {
    font-size: 25px; line-height: 35px; color: var(--navy);
    white-space: nowrap;
  }

  /* ---------- call to action ---------- */
  .cta {
    position: absolute; left: 0; top: 919px; width: 809px; height: 82px;
    background: var(--slate-dark);
    color: var(--white);
    text-align: center;
    padding-top: 12px;
    text-transform: uppercase;
  }
  .cta-lead { font-size: 21px; }
  .cta-action { font-size: 22px; margin-top: 4px; }

  /* ---------- lower band ---------- */
  .lower-band {
    position: absolute; left: 0; top: 1001px; width: 580px; height: 199px;
    background: linear-gradient(180deg, var(--gold-top), var(--gold-deep));
    padding: 4px 12px 0 12px;
  }
  .heartbeat {
    font-size: 27px; line-height: 31px; color: var(--slate-dark);
  }
  .process { list-style: none; margin-top: 6px; }
  .process li {
    font-size: 13.5px; line-height: 14.5px; text-transform: uppercase; color: var(--ink);
  }
  .values {
    position: absolute; left: 580px; top: 1001px; width: 229px; height: 199px;
    background: var(--sky-light);
    display: flex; flex-direction: column; justify-content: center; align-items: center;
    font-family: "Tinos", "Times New Roman", serif;
    font-weight: 700; font-size: 29px; line-height: 1.35; color: var(--navy);
  }
</style>
</head>
<body>
<div class="brochure">
  <div class="top-band"></div>
  <div class="side-stripes"></div>

  <section class="intro-box">
    <h1 class="intro-title">Here to simplify<br>the bookkeeping process</h1>
    <h2 class="intro-sub">What can we do</h2>
    <p class="intro-copy">Allow business owners to spend more time focusing on their core business by providing comprehensive bookkeeping and business consulting services. We provide the financial data and tools that allow businesses to maximize profitability and focus on growth and other areas of their business. We consider our business to be an extension of your business and look forward to the opportunity to exceed your expectations!</p>
  </section>

  <h2 class="why-title">Why Outsource Bookkeeping?</h2>
  <ul class="benefits">
    <li>Save Time</li>
    <li>Save Money</li>
    <li>Expertise</li>
    <li>Focused Staff</li>
    <li>Technology</li>
    <li>Experience</li>
  </ul>

  <div class="services-band" role="img" aria-label="Abstract blue background image"></div>
  <section class="services">
    <h2 class="services-title">Services</h2>
    <ul class="services-list">
      <li>Full Charge Bookkeeping</li>
      <li>Cash Management (Bill Pay &amp; Invoicing)</li>
      <li>&amp; Vendor Management</li>
      <li>Financial Statements</li>
      <li>Account Reconciliations</li>
      <li>Professional liaison</li>
      <li>Business Services</li>
      <li>Exit/Succession Planning</li>
    </ul>
  </section>

  <section class="cta">
    <p class="cta-lead">Let's Talk</p>
    <p class="cta-action">Schedule a no-obligation consultation today</p>
  </section>

  <section class="lower-band">
    <h2 class="heartbeat">The Financial Numbers are the<br>Heart Beat of an organization</h2>
    <ul class="process">
      <li>The Process</li>
      <li>Contact us – we like to hear from you</li>
      <li>No-obligation consultation</li>
      <li>Review current process - identify strengths and weaknesses</li>
      <li>Recommend and implement new bookkeeping process</li>
      <li>Ongoing bookkeeping partnership</li>
      <li>Provide your company with more value and service to keep earning your business (ongoing)</li>
    </ul>
  </section>

  <section class="values">
    <p>Trustworthy</p>
    <p>Experienced</p>
    <p>Reliable</p>
  </section>
</div>
</body>
</html>
```